Keyvane - Premium Club Brochure

Up until now, we've used Canva to create the Brochure we have at-hand, the one attached to this enquiry.

I have been referred to DraftHive by my Business Partner, Marcus Penrovey.

We have recently established a New Real Estate Agency.

This Brochure is our Property Management Membership Brochure, describing the 3x Memberships (Gold, Platinum & Diamond) & outlining the Benefits & Bonuses that are included in these Memberships.

For ALL Pages, we are open to suggestions & other designs/templates/colour schemes.

Target Market(s)

Real Estate - Landlords / Investors

Industry/Entity Type

Real Estate

Font styles to use
Serif
Sans Serif

Colors

Designer to choose colors to be used in the design.

Requirements
Must have
• We would like to do the following:
• - Page 1:
• 1. Include under Email: info@keyvane-demo.com.au
• 2. Include Website under Email (www.keyvane-demo.com.au).
• Website
• www.keyvane-demo.com.au
• 3. The Picture on the right, could we change that Photo to a Block of Apartments & remove the Lines going across the Picture.
• - Page 2
• 1. Create a Border around the Page.
• 2. Heading - Make it stand out more.
• 3. Create Banners for 'Quality Service' & '2.5% Lowest Fees'.
• 4. Categorise the Memberships with these Boarders, please refer to the attachment for example.
• 5. Annual Savings - Make it stand out more.
• - Page 3
• - Page 4
• Please for ALL Fonts, make them the same, we do NOT have the correct font programs to unify them.
Nice to have
• - Page 1:
• Website
• www.keyvane-demo.com.au
• - Page 2:
• When it mentions "2.5% Lowest Fees', please feel free to provide any suggestions, we are open to any suggestions/ideas for this.
Should not have
• Grammar or Spelling errors.

```html
<!DOCTYPE html>
<html lang="en">
<head>
<meta charset="utf-8">
<title>Keyvane – Property Management Membership Brochure</title>
<link href="https://fonts.googleapis.com/css2?family=Roboto+Condensed:wght@400;700&family=Lato:wght@400;700&display=swap" rel="stylesheet">
<style>
  :root{
    --stage:#24282a;
    --slate:#656d6a;
    --charcoal:#262b2b;
    --gold:#fdbf17;
    --white:#ffffff;
    --ink:#1d2020;
    --sky-top:#1f4fd8;
    --sky-bottom:#8fb2e6;
    --brick:#a2483a;
  }
  *{box-sizing:border-box;margin:0;padding:0}
  html,body{width:1200px;height:1200px;overflow:hidden;background:var(--stage)}
  body{position:relative;font-family:"Roboto Condensed",sans-serif;color:var(--ink)}
  h1,h2,h3{font-weight:400}
  .page{position:absolute;overflow:hidden}
  .page-label{position:absolute;width:200px;text-align:center;color:var(--white);font-size:35px;line-height:1}
  .bordered{background:var(--gold)}
  .bordered .inner{position:absolute;inset:7px;background:var(--white)}

  /* Page 1 – cover */
  .cover{left:90px;top:146px;width:460px;height:356px}
  .contact-panel{position:absolute;left:0;top:0;width:152px;height:100%;background:var(--slate);color:var(--white);text-align:center}
  .contact-panel h2{font-size:18px;margin-top:46px}
  .contact-item{position:absolute;left:0;width:100%;font-family:"Lato",sans-serif;font-size:7px}
  .contact-item svg{display:block;margin:0 auto 8px}
  .cover-photo{position:absolute;left:152px;top:0;width:308px;height:290px;background:linear-gradient(160deg,var(--sky-top) 0%,var(--sky-bottom) 45%,#e9e6e0 60%,var(--brick) 100%)}
  .brand{position:absolute;font-weight:400;letter-spacing:.55em;white-space:nowrap}
  .cover .brand{right:6px;top:30px;color:var(--white);font-size:21px}
  .cover-band{position:absolute;left:152px;top:290px;width:308px;height:66px;background:var(--gold);text-align:center;font-size:19px;line-height:22px;padding-top:7px}

  /* Page 2 – membership club */
  .club{left:652px;top:154px;width:458px;height:354px}
  .ribbon-oval{position:absolute;left:17px;top:11px;width:100px;height:58px;border:2px solid var(--gold);border-radius:50%;text-align:center;font-size:17px;line-height:18px;padding-top:9px}
  .ribbon-circle{position:absolute;left:341px;top:9px;width:78px;height:70px;border:2px solid var(--gold);border-radius:50%;text-align:center;font-size:16px;line-height:16px;padding-top:8px}
  .ribbon-circle strong{font-size:22px;display:block;line-height:22px}
  .invite-pill{position:absolute;left:159px;top:9px;width:112px;height:18px;background:var(--charcoal);color:var(--white);border-radius:4px;text-align:center;font-size:11px;line-height:18px}
  .club-heading{position:absolute;left:100px;top:33px;width:230px;text-align:center;line-height:1;white-space:nowrap}
  .club-heading .line1{font-size:17px}
  .club-heading .line2{font-size:23px;font-weight:700;margin-top:3px}
  .tier-card{position:absolute;top:109px;width:112px;height:224px;background:var(--charcoal);border:2px solid var(--gold);color:var(--white)}
  .saving-tab{position:absolute;top:85px;width:80px;height:51px;background:var(--gold);border-radius:4px;text-align:center;font-size:9.5px;line-height:11px;padding-top:3px}
  .saving-tab strong{display:block;font-size:14px;line-height:16px;margin-top:3px}
  .seal{position:absolute;left:13px;top:35px;width:84px;height:84px;border-radius:50%}
  .seal-gold{background:radial-gradient(circle at 40% 35%,#fbe27a,#c79a1c 60%,#8c6a10)}
  .seal-platinum{background:radial-gradient(circle at 40% 35%,#f2f2f2,#a9acae 60%,#6f7274)}
  .seal-diamond{background:radial-gradient(circle at 40% 35%,#ffffff,#b9c4cc 60%,#707b84)}
  .tier-text{position:absolute;left:4px;right:4px;top:128px;font-family:"Lato",sans-serif;font-size:5px;line-height:7px;text-align:center}
  .tier-text .accent{color:var(--gold);white-space:nowrap}
  .tier-text .main{font-size:5.5px;white-space:nowrap}
  .tier-text ul{list-style:none;text-align:left;margin-top:3px}
  .tier-foot{position:absolute;bottom:6px;left:0;width:100%;text-align:center;font-family:"Lato",sans-serif;font-size:5px}

  /* Page 3 – benefits */
  .benefits{left:97px;top:695px;width:463px;height:359px}
  .title-bar{position:absolute;background:var(--charcoal);color:var(--white);text-align:center;white-space:nowrap}
  .benefits .title-bar{left:27px;top:10px;width:406px;height:38px;font-size:23px;line-height:38px}
  .seal-band{position:absolute;left:3px;top:58px;width:443px;height:122px;background:var(--gold)}
  .seal-band .seal{top:3px;width:116px;height:116px}
  .benefit-col{position:absolute;top:196px;font-family:"Lato",sans-serif;font-size:6.2px;line-height:8.3px}
  .benefit-col h3{font-family:"Roboto Condensed",sans-serif;font-size:10px;font-weight:700;margin-bottom:9px}
  .benefit-col ul{padding-left:8px}
  .col-divider{position:absolute;left:221px;top:211px;width:1px;height:110px;background:var(--gold)}

  /* Page 4 – disclaimer */
  .disclaimer{left:673px;top:694px;width:466px;height:361px}
  .disclaimer .title-bar{left:23px;top:10px;width:405px;height:69px;font-size:24px;line-height:29px;padding-top:6px}
  .disclaimer ul{position:absolute;left:27px;top:110px;width:410px;font-family:"Lato",sans-serif;font-size:5.8px;line-height:8.3px;padding-left:8px}
  .disclaimer ul li.plain{list-style:none}
  .disclaimer .brand{left:0;width:100%;text-align:center;top:280px;color:var(--ink);font-size:27px;padding-left:.55em}
</style>
</head>
<body>

<!-- Page 1 -->
<section class="page cover">
  <aside class="contact-panel">
    <h2>Contact US</h2>
    <div class="contact-item" style="top:93px">
      <svg width="14" height="14" viewBox="0 0 14 14"><circle cx="7" cy="7" r="7" fill="#fdbf17"/><path d="M4.5 4l1.5-.5 1 2-1 .8a5 5 0 0 0 1.7 1.7l.8-1 2 1-.5 1.5c-3 .2-5.7-2.5-5.5-5.5z" fill="#fff"/></svg>
      xxxxxxxxxx
    </div>
    <div class="contact-item" style="top:158px">
      <svg width="14" height="14" viewBox="0 0 14 14"><circle cx="7" cy="7" r="7" fill="#fdbf17"/><rect x="4" y="5" width="6" height="4.2" fill="#fff"/><path d="M4 5l3 2.4L10 5" stroke="#fdbf17" stroke-width=".7" fill="none"/></svg>
      info@keyvane-demo.com.au
    </div>
    <div class="contact-item" style="top:225px">
      <svg width="14" height="14" viewBox="0 0 14 14"><circle cx="7" cy="7" r="7" fill="#fdbf17"/><circle cx="7" cy="7" r="3.4" fill="none" stroke="#fff" stroke-width=".8"/><path d="M3.6 7h6.8M7 3.6c-1.6 2-1.6 4.8 0 6.8M7 3.6c1.6 2 1.6 4.8 0 6.8" stroke="#fff" stroke-width=".7" fill="none"/></svg>
      www.keyvane-demo.com.au
    </div>
    <div class="contact-item" style="top:288px">
      <svg width="14" height="14" viewBox="0 0 14 14"><circle cx="7" cy="7" r="7" fill="#fdbf17"/><path d="M7 11s-3-3.2-3-5.2a3 3 0 0 1 6 0C10 7.8 7 11 7 11z" fill="#fff"/><circle cx="7" cy="5.8" r="1" fill="#fdbf17"/></svg>
      Your Location Goes Here
    </div>
  </aside>
  <div class="cover-photo" role="img" aria-label="Photo of a modern block of apartments against a blue sky"></div>
  <div class="brand">KEYVANE</div>
  <div class="cover-band">Property<br>Management Membership</div>
</section>
<div class="page-label" style="left:247px;top:518px">Page -1</div>

<!-- Page 2 -->
<section class="page club bordered">
  <div class="inner">
    <div class="ribbon-oval">Quality<br>Service</div>
    <div class="invite-pill">You Are Invited To</div>
    <h1 class="club-heading"><div class="line1">OUR PROPERTY MANAGEMENT</div><div class="line2">MEMBERSHIP CLUB</div></h1>
    <div class="ribbon-circle"><strong>2.5%</strong>Lowest<br>Fees</div>

    <div class="tier-card" style="left:31px">
      <div class="seal seal-gold" role="img" aria-label="Gold membership seal"></div>
      <div class="tier-text"><div class="accent">1st Level of Premium Membership:</div><div class="main">Complimentary 12-month Membership</div><div class="accent" style="margin-top:3px">GOLD Premium Club BONUS:</div><ul><li>• Property Management Fee: 2.5%.</li><li>• Purchase “Cashback” Bonus: $3,000.00.</li><li>• Selling Fee: 1.65% GST Incl.</li></ul></div>
      <div class="tier-foot">Standard Premium Club Benefits</div>
    </div>
    <div class="saving-tab" style="left:47px">Average<br>Annual Saving Of<strong>$1,014.00</strong></div>

    <div class="tier-card" style="left:167px">
      <div class="seal seal-platinum" role="img" aria-label="Platinum membership seal"></div>
      <div class="tier-text"><div class="accent">Intermediate Level of Premium Membership:</div><div class="main">$5,000.00 Membership Fee (Once Off)</div><div class="accent" style="margin-top:3px">PLATINUM Premium Club BONUS:</div><ul><li>• Member Cash Bonus: 6% of Membership Fee p.a.</li><li>• Property Management Fee: 2.5%*.</li><li>• *3.3% after the first 12 months</li><li>• Purchase “Cashback” Bonus: $4,000.00.</li><li>• Selling Fee: 1.32% GST Incl.</li></ul></div>
      <div class="tier-foot">Standard Premium Club Benefits</div>
    </div>
    <div class="saving-tab" style="left:187px">Average<br>Annual Saving Of<strong>$1,314.00</strong></div>

    <div class="tier-card" style="left:307px">
      <div class="seal seal-diamond" role="img" aria-label="Diamond membership seal"></div>
      <div class="tier-text"><div class="accent">Diamond Level of Premium Membership:</div><div class="main">$7,500.00 Membership Fee (Once Off)</div><div class="accent" style="margin-top:3px">DIAMOND Premium Club BONUS:</div><ul><li>• Member Cash Bonus: 6% of Membership Fee p.a.</li><li>• Property Management Fee: 2.5%.</li><li>• Purchase “Cashback” Bonus: $5,000.00.</li><li>• Selling Fee: 1.1% GST Incl.</li></ul></div>
      <div class="tier-foot">Standard Premium Club Benefits</div>
    </div>
    <div class="saving-tab" style="left:327px">Average<br>Annual Saving Of<strong>$1,464.00</strong></div>
  </div>
</section>
<div class="page-label" style="left:794px;top:526px">Page -2</div>

<!-- Page 3 -->
<section class="page benefits bordered">
  <div class="inner">
    <h1 class="title-bar">PROPERTY MANAGEMENT MEMBERSHIP</h1>
    <div class="seal-band">
      <div class="seal seal-gold" style="left:16px" role="img" aria-label="Gold membership seal"></div>
      <div class="seal seal-platinum" style="left:171px" role="img" aria-label="Platinum membership seal"></div>
      <div class="seal seal-diamond" style="left:316px" role="img" aria-label="Diamond membership seal"></div>
    </div>
    <div class="benefit-col" style="left:26px">
      <h3>PROPERTY MANAGEMENT BENEFITS</h3>
      <ul>
        <li>Discounted Property Management Fee/s.</li>
        <li>14-Days Rent Guarantee Assurance.</li>
        <li>Complimentary End-Of-Month Statement/s.</li>
        <li>Complimentary End-Of-Year Statement/s.</li>
        <li>Complimentary Outgoing-Payments Service.</li>
        <li>Complimentary Trade-Services Liaison.</li>
        <li>Complimentary Tribunal Representation/s.</li>
        <li>Complimentary Half-Yearly Inspections.</li>
        <li>Complimentary Half-Yearly Report with Photos.</li>
        <li>Complimentary Term Rent Review.</li>
        <li>Complimentary Landlord Insurance Liaison.</li>
        <li>Complimentary Depreciation Report Liaison.</li>
        <li>Complimentary Tax Gearing Calculation Guide.</li>
        <li>Complimentary Support to your Tax Agent/Accountant.</li>
      </ul>
    </div>
    <div class="col-divider"></div>
    <div class="benefit-col" style="left:273px">
      <h3>PURCHASE &amp; SALES BENEFITS</h3>
      <ul>
        <li>“Cashback” Bonus on Purchase.</li>
        <li>Complimentary Legal Fee for Purchase.</li>
        <li>FREE Market Analysis Report.</li>
        <li>Complimentary Bank Valuation.</li>
        <li>Discounted Selling Fee.</li>
        <li>Complimentary Auctioneer Fee.</li>
        <li>FREE Mortgage Consultation.</li>
        <li>FREE Mortgage Loan Health Check.</li>
        <li>FREE 1st Home Buyer Consultation.</li>
        <li>FREE Wealth Creation in Property Investment Consultation.</li>
        <li>FREE Equity-Share Investment Advisory.</li>
        <li>FREE SMSF in Property Investment Consultation.</li>
        <li>Complimentary Property Investment Workshop.</li>
        <li>Complimentary Property Investment Seminar.</li>
      </ul>
    </div>
  </div>
</section>
<div class="page-label" style="left:246px;top:1074px">Page -3</div>

<!-- Page 4 -->
<section class="page disclaimer bordered">
  <div class="inner">
    <h1 class="title-bar">PROPERTY MANAGEMENT MEMBERSHIP<br>Disclaimer</h1>
    <ul>
      <li>Keyvane Group Pty Ltd is a FULLY Licensed Real Estate Agent.</li>
      <li>Keyvane Group &amp; its subsidiary Businesses operate under the 1 &amp; same ABN.</li>
      <li>Memberships can be upgraded with a written Notice issued to Keyvane Group, upgrade will take into affect after 1-Month.</li>
      <li>Memberships can be cancelled with a written Notice issued to Keyvane Group, cancellation will take into affect after 1-Month &amp; a FULL Refund of Membership Fees will be made (only applicable to Platinum and Diamond Membership).</li>
      <li>Keyvane Consultation &amp; Advisory Services are of Information Sharing basis and Client MUST conduct their own enquiries with the relevant Qualified Professionals.</li>
      <li>Keyvane Group's Affiliated &amp; Referred Professionals are deemed to be properly qualified and Client MUST verify on their own discretion &amp; accord.</li>
      <li>Keyvane Group CANNOT be held accountable and/or responsible for the actions of other Entities.</li>
      <li>ALL Benefits are subject to Terms &amp; Conditions of KEYVANE Premium Club.</li>
      <li>Terms &amp; Conditions will be issued to every Member and available on Keyvane Website: www.keyvane-demo.com.au</li>
      <li>ALL Benefits &amp; Bonuses are ONLY applicable to Residential Properties.</li>
      <li>Bank Valuation/s are subject to Bank/s' discretion &amp; may NOT be provided as Hard-Copy.</li>
      <li>Benefits and Bonuses may be amended with Notice.</li>
      <li class="plain">Membership Fee/s are FULLY Refunded &amp; guaranteed by Keyvane Group Pty Ltd.</li>
      <li class="plain">ALL Benefits &amp; Bonuses are to be terminated on the day of Notice &amp; NO Pro-Rata will be given.</li>
    </ul>
    <div class="brand">KEYVANE</div>
  </div>
</section>
<div class="page-label" style="left:794px;top:1080px">Page -4</div>

</body>
</html>
```